Bride Basecamp

I am looking for a design for http://www.bridebasecamp.co.uk/ its a joomla site and I am going to set up with the same mods as our stag version http://www.groomnightout.co.uk/ you will see on groomnight how all the menus look and are positioned. Here is an example of a activity page http://www.groomnightout.co.uk/activity/white-water-rafting-in-perthshire.html which comes from Kiln.

The design needs to be built for responsive layout. The brand look and feel needs to be 100% for the female market.

We can accept the design in photoshop or something similar

Please ask questions if you require more information.

some examples of hen sites

http://www.maidenmerry.co.uk/

```html
<!DOCTYPE html>
<html lang="en">
<head>
<meta charset="utf-8">
<title>Bride Basecamp – Hen Day, Night and Weekend Activities</title>
<link href="https://fonts.googleapis.com/css2?family=Open+Sans:wght@400;600;700;800&family=Roboto+Condensed:wght@700&display=swap" rel="stylesheet">
<style>
:root{
  --orange:#f26522;
  --blue:#1b7fc4;
  --blue-dark:#14609a;
  --blue-pale:#eaf4fb;
  --line:#c9dcea;
  --text:#555;
  --grey:#d4d4d4;
  --green:#00b67a;
  --page:#ffffff;
  --footer:#1e88c7;
  --footer-low:#e9eef2;
}
*{box-sizing:border-box;margin:0;padding:0}
html,body{width:1200px;height:2584px;overflow:hidden}
body{background:var(--page);font-family:"Open Sans",Arial,sans-serif;color:var(--text);font-size:13px;line-height:1.5;position:relative}
.wrap{position:absolute;left:32px;width:1136px}
h2{font-family:"Roboto Condensed","Arial Narrow",sans-serif;color:var(--blue);font-size:20px;text-transform:uppercase;letter-spacing:.3px}
/* header */
.site-header{top:0;height:48px;display:flex;align-items:center;justify-content:space-between}
.brand{font-family:"Open Sans",sans-serif;font-weight:800;font-size:26px;color:var(--orange);letter-spacing:.5px;text-transform:uppercase}
.search{display:flex}
.search span{width:190px;height:26px;border:1px solid #bbb;font-size:11px;color:#999;padding:4px 8px}
.search b{width:26px;height:26px;background:var(--orange);display:flex;align-items:center;justify-content:center}
.main-nav{top:48px;height:28px;background:var(--blue);display:flex;padding-left:20px}
.main-nav a{color:#fff;font-size:12px;font-weight:600;text-decoration:none;text-transform:uppercase;padding:5px 26px}
.hero{top:76px;height:296px;background:linear-gradient(120deg,#c98a5a,#e8c3a0 40%,#8c6b55 70%,#d9b08a);}
.hero .dots{position:absolute;left:20px;bottom:16px;display:flex;gap:6px}
.hero .dots i{width:10px;height:10px;border-radius:50%;background:#fff;opacity:.6}
.hero .dots i:first-child{opacity:1}
.hero .welcome{position:absolute;right:0;bottom:12px;background:rgba(20,20,20,.75);color:#fff;font-family:"Roboto Condensed",sans-serif;font-size:22px;padding:6px 24px;text-transform:uppercase}
/* intro */
.intro{top:388px;height:160px}
.intro h2{margin-bottom:10px}
.intro p{width:820px;margin-bottom:10px}
.partner{position:absolute;right:20px;top:92px;display:flex;align-items:center;gap:10px;font-weight:800;font-size:30px;color:#222}
.partner i{width:34px;height:34px;background:#8cc63f;border-radius:50%}
/* book now */
.book{top:564px;height:412px;border:1px solid var(--line);background:#f6f9fc;padding:14px 22px}
.book h2{margin-bottom:14px}
.dest-grid{display:grid;grid-template-columns:repeat(4,1fr);gap:22px 24px}
.dest{height:152px;position:relative}
.dest span{position:absolute;left:0;right:0;bottom:0;background:rgba(0,0,0,.6);color:#fff;font-weight:700;font-size:12px;padding:3px 8px;text-transform:uppercase}
.d1{background:linear-gradient(#7aa9d6,#4a6f8f)}.d2{background:linear-gradient(#8fc8ea,#d9c28a)}
.d3{background:linear-gradient(#5d8fc2,#3b5b7a)}.d4{background:linear-gradient(#a4b7c9,#6c7f54)}
.d5{background:linear-gradient(#6f9ac4,#555)}.d6{background:linear-gradient(#9bb3cc,#7b6b5a)}
.d7{background:linear-gradient(#7fb0d8,#8a7260)}.d8{background:linear-gradient(#5886b8,#c9a268)}
/* video */
.video{top:1040px;height:444px;border-top:3px solid var(--blue);padding-top:12px}
.video h3{color:var(--blue-dark);font-size:14px;font-weight:700;text-transform:uppercase;margin:6px 0 4px}
.video p{font-size:12px;width:820px}
.player{margin:22px auto 0;width:520px;height:272px;background:#111;padding:24px 0 0;position:relative}
.player .bar{position:absolute;top:4px;left:10px;color:#ddd;font-size:11px}
.player .screen{height:248px;background:linear-gradient(#fffef2,#f3efb0);display:flex;align-items:center;justify-content:center}
/* reviews */
.reviews{top:1500px;height:840px}
.reviews h2{margin-bottom:10px}
.panel{margin:0 88px;border:1px solid var(--line);background:var(--blue-pale);padding:16px 30px 24px;height:796px}
.score{text-align:center;margin-bottom:14px}
.score strong{display:block;color:var(--blue-dark);font-size:20px;font-weight:800}
.score small{font-size:11px}
.stars{display:inline-flex;gap:3px;vertical-align:middle}
.stars i{width:14px;height:14px;background:var(--green)}
.stars.lg i{width:22px;height:22px}
.cols{display:grid;grid-template-columns:1fr 1fr;gap:40px}
.col{background:#fff;border:1px solid var(--line);padding:12px 14px}
.col h4{color:var(--blue);font-size:13px;border-bottom:1px solid var(--line);padding-bottom:6px;margin-bottom:10px}
.review{display:flex;gap:12px;height:146px;border-bottom:1px solid #eee;padding-top:8px}
.review:last-child{border:0}
.avatar{width:62px;height:62px;background:var(--grey);flex:none}
.meta{font-size:9px;color:#888;margin-top:4px;width:62px}
.review h5{color:var(--blue);font-size:11px;margin:4px 0 2px;text-transform:uppercase}
.review p{font-size:10.5px;line-height:1.45}
/* footer */
.site-footer{position:absolute;left:0;top:2400px;width:1200px;height:184px;background:var(--footer-low)}
.footer-bar{margin:0 32px;height:84px;background:var(--footer);color:#fff;display:flex;justify-content:space-between;padding:12px 20px;font-size:12px}
.social{display:flex;gap:6px;margin-top:8px}
.social i{width:22px;height:22px;background:#fff;opacity:.85}
.legal{text-align:right;font-size:10px;width:560px}
.footer-links{text-align:center;font-size:11px;color:#555;padding:14px}
.footer-links a{color:#555;text-decoration:none;margin:0 6px}
</style>
</head>
<body>
<header class="wrap site-header">
  <div class="brand">Bride Basecamp</div>
  <div class="search"><span>Enter search</span><b><svg width="12" height="12" viewBox="0 0 12 12"><circle cx="5" cy="5" r="3.5" fill="none" stroke="#fff" stroke-width="1.6"/><line x1="7.6" y1="7.6" x2="11" y2="11" stroke="#fff" stroke-width="1.8"/></svg></b></div>
</header>
<nav class="wrap main-nav">
  <a>Home</a><a>About us</a><a>Services</a><a>Hen packages</a><a>News</a><a>Blog</a><a>Contact us</a>
</nav>
<section class="wrap hero" role="img" aria-label="Group of women celebrating a hen party with drinks">
  <div class="dots"><i></i><i></i><i></i><i></i><i></i></div>
  <div class="welcome">Welcome to our site</div>
</section>
<section class="wrap intro">
  <h2>Bride Basecamp - Hen Day, Night and Weekend Activities</h2>
  <p>Bride Basecamp is the place to start if you want to put together a great hen party. We have hundreds of activities across the country and every year we help thousands of brides and their friends plan the perfect celebration. Whether you want a relaxing spa day, a cocktail masterclass or a full weekend away, our team will build a package around you.</p>
  <p>We can arrange it all on weekends or just one night, just let us know a few details and we will do all the rest. We can even create your own friends for the money rather than you trying to do it.</p>
  <div class="partner"><i></i>Party Pals</div>
</section>
<section class="wrap book">
  <h2>Book now</h2>
  <div class="dest-grid">
    <div class="dest d1" role="img" aria-label="Liverpool waterfront"><span>Liverpool</span></div>
    <div class="dest d2" role="img" aria-label="Bournemouth beach"><span>Bournemouth</span></div>
    <div class="dest d3" role="img" aria-label="Brighton pier"><span>Brighton</span></div>
    <div class="dest d4" role="img" aria-label="Bristol bridge"><span>Bristol</span></div>
    <div class="dest d5" role="img" aria-label="Cardiff bay"><span>Cardiff</span></div>
    <div class="dest d6" role="img" aria-label="Edinburgh castle"><span>Edinburgh</span></div>
    <div class="dest d7" role="img" aria-label="Leeds city centre"><span>Leeds</span></div>
    <div class="dest d8" role="img" aria-label="Newcastle quayside"><span>Newcastle</span></div>
  </div>
</section>
<section class="wrap video">
  <h2>Video</h2>
  <h3>Rather than build a website with 1000's of pages that you will never read we thought "hey, let's make it easy"</h3>
  <p>So all you have to do is fill in the short form below and we will email you details and suggestions. If however you really want to read up on everything then visit our main site Bride Basecamp now.</p>
  <div class="player">
    <div class="bar">Hear The Bride Basecamp Story | Party Pals</div>
    <div class="screen" role="img" aria-label="Video thumbnail explaining how to book a hen party">
      <svg width="70" height="70" viewBox="0 0 70 70"><circle cx="35" cy="35" r="32" fill="#222"/><polygon points="28,22 50,35 28,48" fill="#fff"/></svg>
    </div>
  </div>
</section>
<section class="wrap reviews">
  <h2>Customer reviews</h2>
  <div class="panel">
    <div class="score">
      <strong>EXCELLENT</strong>
      <span class="stars lg"><i></i><i></i><i></i><i></i><i></i></span><br>
      <small>715 customers have written a review on ReviewHub</small>
    </div>
    <div class="cols">
      <div class="col">
        <h4>Selected Reviews</h4>
        <div class="review"><div><div class="avatar"></div><div class="meta">Georgia 12th Dec confirmed purchase</div></div><div><span class="stars"><i></i><i></i><i></i><i></i><i></i></span><h5>Excellent from booking to day</h5><p>What a wonderful time we had. It was a Christmas present from my grandparents and it all went so smoothly from start to finish. We had a great fun and will definitely go back again.</p></div></div>
        <div class="review"><div><div class="avatar"></div><div class="meta">Sophie 9th Dec confirmed purchase</div></div><div><span class="stars"><i></i><i></i><i></i><i></i><i></i></span><h5>Helpful, friendly contacts who assisted us</h5><p>I would have booked a fairly short notice. Received prompt email reply and follow up phone calls to get all details arranged in good time.</p></div></div>
        <div class="review"><div><div class="avatar"></div><div class="meta">Hannah 2nd Dec confirmed purchase</div></div><div><span class="stars"><i></i><i></i><i></i><i></i><i></i></span><h5>Alles is lieben</h5><p>I bookmarked this page to find out a lot of information and then responded straight away. Gave me all the information I needed and were careful to pass the deposit in very easy parts.</p></div></div>
        <div class="review"><div><div class="avatar"></div><div class="meta">Emily 28th Nov confirmed purchase</div></div><div><span class="stars"><i></i><i></i><i></i><i></i><i></i></span><h5>Excellent from booking to day</h5><p>What a wonderful time we had. It was a Christmas present from my grandparents and it all went so smoothly from start to finish. We will definitely go back again.</p></div></div>
      </div>
      <div class="col">
        <h4>Selected Reviews</h4>
        <div class="review"><div><div class="avatar"></div><div class="meta">Lucy 11th Dec confirmed purchase</div></div><div><span class="stars"><i></i><i></i><i></i><i></i><i></i></span><h5>Lovely team who simply sorted it all</h5><p>What a wonderful time we had. It was a Christmas present from my grandparents and it all went smoothly from start to finish. We had great fun and will definitely go back again.</p></div></div>
        <div class="review"><div><div class="avatar"></div><div class="meta">Chloe 6th Dec confirmed purchase</div></div><div><span class="stars"><i></i><i></i><i></i><i></i><i></i></span><h5>Friendly, quick and very helpful</h5><p>I would have booked a fairly short notice. Received prompt email reply and follow up phone calls to get all details arranged in good time.</p></div></div>
        <div class="review"><div><div class="avatar"></div><div class="meta">Megan 30th Nov confirmed purchase</div></div><div><span class="stars"><i></i><i></i><i></i><i></i><i></i></span><h5>The standard route of planning</h5><p>I bookmarked this page to find out a lot of information and then responded straight away. Gave me all the information I needed and were careful to pass the deposit.</p></div></div>
        <div class="review"><div><div class="avatar"></div><div class="meta">Amy 24th Nov confirmed purchase</div></div><div><span class="stars"><i></i><i></i><i></i><i></i><i></i></span><h5>There are many variations of packages</h5><p>What a wonderful time we had. It was a Christmas present from my grandparents and it all went smoothly. We had great fun and will definitely book again.</p></div></div>
      </div>
    </div>
  </div>
</section>
<footer class="site-footer">
  <div class="footer-bar">
    <div>Connect with us<div class="social"><i></i><i></i><i></i><i></i></div></div>
    <div class="legal">Call us on 0123 456 7890 Copyright 2014 Bride Basecamp Ltd. All rights reserved. Registered in England and Wales, company number 01234567. Registered office: 1 Sample Street, Exampletown, AB1 2CD. Terms and conditions apply.</div>
  </div>
  <div class="footer-links"><a>Home</a>|<a>About Us</a>|<a>Services</a>|<a>Hen Packages</a>|<a>News</a>|<a>Blog</a>|<a>Contact Us</a><br>Copyright © 2014 Bride Basecamp. All Rights Reserved.</div>
</footer>
</body>
</html>
```